Luminously Grounded Vitality

We want to design a business card that is modern and appealing for an innovative psychedelic telemedicine company that provides at-home ketamine-assisted therapy along with wellness, longevity, and anti-aging medicines. We want to use our deep purple and white plus other colors you can find on our website. We don't have any strict brand guidelines yet so feel free to get creative. We want a very professional, but technology first modern design that will instill trust, peace, calm, but also be attractive to investors in the healthcare and SaaS space.

```html
<!DOCTYPE html>
<html lang="en">
<head>
<meta charset="utf-8">
<title>Luminously Grounded Vitality – Business Card</title>
<link rel="stylesheet" href="https://fonts.googleapis.com/css2?family=Marcellus&display=swap">
<style>
  :root {
    --deep-purple: #7f69a7;
    --orchid: #b073a1;
    --lavender: #9b88bb;
    --white: #ffffff;
  }
  html, body {
    margin: 0;
    padding: 0;
    width: 1200px;
    height: 686px;
    overflow: hidden;
    background: var(--white);
  }
  .card {
    position: relative;
    width: 1200px;
    height: 686px;
    background: var(--white);
    overflow: hidden;
  }
  .card__waves {
    position: absolute;
    inset: 0;
    width: 1200px;
    height: 686px;
  }
  .wave--purple { fill: var(--deep-purple); }
  .wave--orchid { fill: var(--orchid); }
  .contact-icon { fill: none; stroke: var(--white); stroke-width: 3.5; stroke-linecap: round; stroke-linejoin: round; }
  .brand-mark {
    position: absolute;
    left: 562px;
    top: 250px;
    width: 62px;
    height: 62px;
    border-radius: 50%;
    background: var(--lavender);
  }
  .brand-name {
    position: absolute;
    left: 0;
    width: 1200px;
    top: 418px;
    margin: 0;
    text-align: center;
    font-family: "Marcellus", serif;
    font-weight: 400;
    font-size: 76px;
    line-height: 1;
    color: var(--orchid);
    letter-spacing: 0.5px;
  }
</style>
</head>
<body>
  <main class="card">
    <svg class="card__waves" viewBox="0 0 1914 1094" preserveAspectRatio="none" aria-hidden="true">
      <defs>
        <filter id="wave-shadow" x="-20%" y="-20%" width="140%" height="140%">
          <feDropShadow dx="-6" dy="4" stdDeviation="10" flood-color="#000" flood-opacity="0.18"/>
        </filter>
      </defs>
      <!-- top-left wave -->
      <path class="wave--orchid" d="M0,0 L795,0 C700,150 580,250 450,290 C330,330 280,420 240,560 C200,700 190,860 150,950 C110,1040 60,1068 0,1068 Z"/>
      <path class="wave--purple" d="M0,0 L690,0 C620,110 520,190 400,225 C280,260 230,380 195,560 C160,740 140,880 90,960 C60,1005 30,1020 0,1025 Z"/>
      <!-- bottom-right wave -->
      <g filter="url(#wave-shadow)">
        <path class="wave--orchid" d="M1914,25 C1830,25 1760,120 1730,250 C1690,430 1660,640 1600,720 C1560,770 1520,790 1460,805 C1330,850 1200,950 1120,1094 L1914,1094 Z"/>
      </g>
      <path class="wave--purple" d="M1914,70 C1850,90 1790,180 1760,320 C1720,500 1700,700 1630,790 C1600,830 1560,855 1510,868 C1400,900 1290,990 1225,1094 L1914,1094 Z"/>
      <!-- contact icons -->
      <g class="contact-icons">
        <g class="contact-icon contact-icon--mail">
          <rect x="1642" y="894" width="35" height="40" rx="2"/>
          <path d="M1642,897 L1659.5,918 L1677,897 M1642,932 L1655,914 M1677,932 L1664,914"/>
        </g>
        <g class="contact-icon contact-icon--web">
          <circle cx="1718" cy="914" r="18"/>
          <ellipse cx="1718" cy="914" rx="8" ry="18"/>
          <path d="M1718,896 L1718,932 M1701,908 L1735,908 M1701,920 L1735,920"/>
        </g>
        <g class="contact-icon contact-icon--phone">
          <path d="M1763,895 C1756,898 1756,912 1763,922 C1769,931 1776,936 1780,931 L1777,925 L1771,926 C1767,921 1764,914 1764,908 L1769,905 L1766,895 Z"/>
          <path d="M1770,900 C1774,901 1776,904 1777,908 M1771,893 C1778,894 1782,899 1783,906"/>
        </g>
        <g class="contact-icon contact-icon--location">
          <path d="M1819,934 C1812,922 1810,916 1810,911 A9,9 0 0 1 1828,911 C1828,916 1826,922 1819,934 Z"/>
          <circle cx="1819" cy="911" r="3"/>
        </g>
      </g>
    </svg>

    <span class="brand-mark" aria-hidden="true"></span>
    <h1 class="brand-name">Luminously</h1>
  </main>
</body>
</html>
```